Staff Newsletter Template Image

We are looking for two .jpg images that we can put into a Word document and use for our staff newsletter. We will then add content using text boxes.
Attached is the current template which works for the columns and size that we need but we just want a fresh new design.
The Word document shows how we use it.
The name will stay the same - Team upBeat but can be a different look to the current one.

Target Market(s)

Sales team

Colors

Designer to choose colors to be used in the design.

Requirements
Must have
• Colours will be green, grey and white, possibly cream if needed. All from the guidelines.
• I have attached our brand guidelines which shows design elements and fonts for our brand. Also attached is brand guidelines for one of our product lines as we would like to use the same green.
• It needs to be nice to look at and motivational for our team

```html
<!DOCTYPE html>
<html lang="en">
<head>
<meta charset="utf-8">
<title>Team upBeat – Newsletter Pages</title>
<link rel="stylesheet" href="https://fonts.googleapis.com/css2?family=Raleway:wght@300&display=swap">
<style>
  :root {
    --canvas-bg: #dedede;
    --brand-green: #8dc641;
    --brand-green-deep: #5a8a2a;
    --brand-grey: #4d4b4c;
    --paper-white: #ffffff;
  }
  html, body {
    margin: 0;
    padding: 0;
    width: 1200px;
    height: 1000px;
    overflow: hidden;
    background: var(--canvas-bg);
  }
  .newsletter-spread {
    position: relative;
    width: 1200px;
    height: 1000px;
  }
  .page {
    position: absolute;
    top: 183px;
    width: 449px;
    height: 634px;
  }
  .page--front { left: 121px; }
  .page--back { left: 631px; }
  .page svg {
    display: block;
    width: 100%;
    height: 100%;
  }
  .column--light { fill: var(--paper-white); }
  .column--dark { fill: var(--brand-grey); }
  .wave--grey { fill: var(--brand-grey); }
  .wave--white { fill: var(--paper-white); }
  .wave--green { fill: var(--brand-green); }
  .masthead-title {
    font-family: "Raleway", sans-serif;
    font-weight: 300;
    font-size: 60px;
    fill: var(--brand-grey);
  }
</style>
</head>
<body>
<main class="newsletter-spread">

  <section class="page page--front" aria-label="Newsletter front page">
    <svg viewBox="0 0 673 951" preserveAspectRatio="none">
      <defs>
        <linearGradient id="header-green" x1="0" y1="0" x2="0" y2="1">
          <stop offset="0" stop-color="var(--brand-green-deep)"/>
          <stop offset="0.5" stop-color="var(--brand-green)"/>
          <stop offset="1" stop-color="var(--brand-green)"/>
        </linearGradient>
      </defs>
      <rect class="column--light" x="0" y="0" width="336" height="951"/>
      <rect class="column--dark" x="336" y="0" width="337" height="951"/>
      <path fill="url(#header-green)" d="M0,0 H673 V156 C600,185 520,200 420,196 C390,194 360,190 336,182 C260,158 200,120 119,123 C60,125 20,145 0,168 Z"/>
      <path class="wave--grey" d="M0,168 C20,145 60,125 119,123 C200,120 260,158 336,182 V211 C280,200 200,160 109,153 C60,150 20,160 0,172 Z"/>
      <path class="wave--white" d="M336,182 C360,190 390,194 420,196 C520,200 600,185 673,156 V158 C600,190 520,222 439,221 C400,220 360,216 336,211 Z"/>
      <text class="masthead-title" x="336" y="116" text-anchor="middle">Team upBeat</text>
    </svg>
  </section>

  <section class="page page--back" aria-label="Newsletter back page">
    <svg viewBox="0 0 673 951" preserveAspectRatio="none">
      <rect class="column--light" x="0" y="0" width="336" height="951"/>
      <rect class="column--dark" x="336" y="0" width="337" height="951"/>
      <g transform="translate(0,718)">
        <path class="wave--grey" d="M0,168 C20,145 60,125 119,123 C200,120 260,158 336,182 V211 C280,200 200,160 109,153 C60,150 20,160 0,172 Z"/>
        <path class="wave--white" d="M336,182 C360,190 390,194 420,196 C520,200 600,185 673,156 V158 C600,190 520,222 439,221 C400,220 360,216 336,211 Z"/>
        <path class="wave--green" d="M0,172 C20,160 60,150 109,153 C200,160 280,200 336,211 C360,216 400,220 439,221 C520,222 600,190 673,158 V233 H0 Z"/>
      </g>
    </svg>
  </section>

</main>
</body>
</html>
```